Business IT Services Billboard to attract local small businesses

We are Brivolane, a premier Managed Service Provider (MSP) specializing in comprehensive IT services and VOIP phone solutions exclusively for businesses. Our goal is to create a dynamic and visually engaging billboard advertisement that not only highlights our cutting-edge IT solutions but also emphasizes our state-of-the-art VOIP phone services. This billboard should communicate our commitment to providing innovative, reliable, and holistic technology solutions.
Target Market(s)
small business
Industry/Entity Type
Information Technology
Colors
Designer to choose colors to be used in the design.
Look and feel
Each slider illustrates characteristics of the customer's brand and the style your logo design should communicate.

```html
<!DOCTYPE html>
<html lang="en">
<head>
<meta charset="utf-8">
<title>Brivolane Billboard</title>
<link href="https://fonts.googleapis.com/css2?family=Poppins:wght@200;300;400;700&display=swap" rel="stylesheet">
<style>
  :root {
    --stage: #a7a7a7;
    --brand-blue: #1478c0;
    --ink: #000000;
    --paper: #ffffff;
    --silver: #9a9da3;
    --photo-light: #eceae6;
    --photo-mid: #d8d3cb;
    --photo-warm: #c9b79a;
  }
  html, body {
    margin: 0;
    padding: 0;
    width: 1200px;
    height: 1200px;
    overflow: hidden;
    background: var(--stage);
  }
  .billboard {
    position: absolute;
    left: 50px;
    top: 325px;
    width: 1100px;
    height: 550px;
    box-shadow: 0 2px 6px rgba(0,0,0,0.35);
  }
  .billboard svg { display: block; width: 100%; height: 100%; }
  .brand-name {
    font-family: "Poppins", sans-serif;
    font-weight: 700;
    fill: var(--brand-blue);
    letter-spacing: 2px;
  }
  .headline {
    font-family: "Poppins", sans-serif;
    fill: var(--paper);
    font-size: 68px;
  }
  .headline .light { font-weight: 200; }
  .headline .bold { font-weight: 700; }
  .headline .accent { font-weight: 700; fill: var(--brand-blue); }
  .tagline {
    font-family: "Poppins", sans-serif;
    font-weight: 300;
    font-size: 29px;
    fill: var(--paper);
  }
  .cta {
    font-family: "Poppins", sans-serif;
    font-weight: 300;
    font-size: 32px;
    fill: var(--paper);
  }
  .cta .url { font-weight: 700; }
</style>
</head>
<body>
  <div class="billboard">
    <svg viewBox="0 0 1383 690" preserveAspectRatio="none" xmlns="http://www.w3.org/2000/svg">
      <defs>
        <linearGradient id="photoTone" x1="0" y1="0" x2="1" y2="1">
          <stop offset="0" stop-color="var(--photo-light)"/>
          <stop offset="0.55" stop-color="var(--photo-mid)"/>
          <stop offset="1" stop-color="var(--photo-warm)"/>
        </linearGradient>
      </defs>

      <rect class="canvas-base" x="0" y="0" width="1383" height="690" fill="var(--paper)"/>

      <path class="photo-area" role="img"
            aria-label="Photo of a smiling support technician wearing a headset, typing at a computer in a bright office"
            d="M700 0 H1383 V565 H745 L640 470 Q728 400 728 330 Q718 250 580 138 Z"
            fill="url(#photoTone)"/>

      <path class="photo-edge" d="M700 0 L580 138 Q718 250 728 330 Q728 400 640 470 L745 565"
            fill="none" stroke="var(--silver)" stroke-width="6"/>

      <path class="headline-band" d="M0 155 H555 L675 262 Q712 330 690 405 L585 530 H0 Z" fill="var(--ink)"/>

      <path class="tagline-band" d="M0 530 H590 L750 690 H0 Z" fill="var(--brand-blue)"/>

      <path class="cta-band" d="M725 565 H1383 V690 H850 Z" fill="var(--ink)"/>

      <text class="brand-name" x="87" y="103" font-size="56">Brivolane</text>

      <text class="headline">
        <tspan class="light" x="87" y="245">SEAMLESS</tspan>
        <tspan class="bold" x="87" y="308">TECHNOLOGY</tspan>
        <tspan class="accent" x="87" y="370">SOLUTIONS</tspan>
        <tspan class="light" x="87" y="432">FOR MODERN</tspan>
        <tspan class="bold" x="87" y="495">BUSINESSES</tspan>
      </text>

      <text class="tagline">
        <tspan x="87" y="597">Innovative IT and VOIP Solutions</tspan>
        <tspan x="87" y="633">Tailored for Your Business Success.</tspan>
      </text>

      <text class="cta" text-anchor="middle">
        <tspan x="1070" y="617">Transform Your Tech Today</tspan>
        <tspan x="1070" y="657">at <tspan class="url">www.brivolane.com</tspan></tspan>
      </text>
    </svg>
  </div>
</body>
</html>
```